Fahrzeugbeschriftung für Badsanierungen
Zielgruppe
Wir sanieren Bäder incl. aller hierzu erforderlichen Gewerke wie Heizung, Sanitär, Elektro, Wandputz, Trockenbau und Fliesen. Unsere Zielgruppe sind Menschen, die ihr Bad sanieren oder überholen lassen wollen
Aufgabenstellung
Es soll eine moderne Folierung erfolgen, gerne etwas größer, mit großem Bild eines sanierten Bades, oder verschiedener Badausstattungen. Das Logo und die Kontaktdaten sollen ersichtlich sein. Bitte keine einfache Beschriftung
Es handelt sich um einen Molt Varena Kastenwagen Trend, ohne Fenster Länge 3 Höhe 2
Das im Anschluss aufgeführte Logo soll eine andere Beschriftung erhalten. Anstatt Handwerksunternehmen soll es 'Badsanierungen' heißen

```html
<!DOCTYPE html>
<html lang="de">
<head>
<meta charset="utf-8">
<title>Wendelkamp Badsanierungen – Fahrzeugbeschriftung</title>
<link rel="stylesheet" href="https://fonts.googleapis.com/css2?family=Fira+Sans:ital,wght@0,500;0,600;1,600;1,700&display=swap">
<style>
  :root {
    --ink: #3a4658;
    --body: #f4f4f2;
    --band: #1e1f22;
    --stripe-dark: #3d4a5c;
    --stripe-grey: #a7abae;
    --glass: #5b5f64;
    --tyre: #202124;
    --hub: #c9cbcd;
    --tail: #b3231d;
    --backdrop: #ffffff;
  }
  html, body {
    margin: 0;
    width: 1200px;
    height: 540px;
    overflow: hidden;
    background: var(--backdrop);
  }
  .wrap-canvas {
    display: block;
    width: 1200px;
    height: 540px;
  }
  .headline { font: italic 700 52px "Fira Sans", sans-serif; fill: var(--ink); }
  .brand-name { font: 600 46px "Fira Sans", sans-serif; fill: var(--ink); letter-spacing: 1px; }
  .phone-number { font: italic 700 38px "Fira Sans", sans-serif; fill: var(--ink); letter-spacing: 1px; }
  .address { font: italic 600 16px "Fira Sans", sans-serif; fill: var(--ink); }
  .website { font: italic 600 26px "Fira Sans", sans-serif; fill: var(--ink); }
</style>
</head>
<body>
<svg class="wrap-canvas" viewBox="0 0 1780 800" preserveAspectRatio="xMidYMid meet" xmlns="http://www.w3.org/2000/svg">
  <defs>
    <linearGradient id="bath-photo-tone" x1="0" y1="0" x2="1" y2="1">
      <stop offset="0" stop-color="#e6e6e4"/>
      <stop offset="0.5" stop-color="#d8d4cf"/>
      <stop offset="1" stop-color="#c9c3bb"/>
    </linearGradient>
    <clipPath id="body-clip">
      <path d="M60,520 L80,430 Q120,380 230,350 L330,320 Q450,160 560,100 Q620,62 720,58 L1620,38 Q1680,40 1690,60 L1700,520 Z"/>
    </clipPath>
  </defs>

  <!-- van body -->
  <path class="van-body" fill="var(--body)" stroke="#cfcfcf" stroke-width="2"
        d="M60,520 L80,430 Q120,380 230,350 L330,320 Q450,160 560,100 Q620,62 720,58 L1620,38 Q1680,40 1690,60 L1700,520 Z"/>

  <g clip-path="url(#body-clip)">
    <!-- bathroom photo area -->
    <path role="img" aria-label="Foto eines sanierten Bades mit Waschtisch, Badewanne und einer Frau im Bademantel"
          fill="url(#bath-photo-tone)"
          d="M1265,30 L1710,30 L1710,530 L1060,530 Q1180,300 1265,30 Z"/>
    <!-- sweeping stripes -->
    <path class="stripe-grey" fill="var(--stripe-grey)" d="M1200,30 L1232,30 Q1150,320 1060,530 L1030,530 Q1120,320 1200,30 Z"/>
    <path class="stripe-dark" fill="var(--stripe-dark)" d="M1218,30 L1256,30 Q1175,320 1082,530 L1040,530 Q1140,320 1218,30 Z"/>
  </g>

  <!-- panel seams -->
  <g class="seams" stroke="#c4c4c4" stroke-width="2" fill="none">
    <path d="M700,62 L705,525"/>
    <path d="M1135,48 L1140,520"/>
    <path d="M360,300 L362,520"/>
  </g>

  <!-- cab window -->
  <path class="cab-window" fill="var(--band)" d="M375,300 L515,175 L665,168 L665,372 L380,405 Z"/>
  <path class="cab-glass" fill="var(--glass)" d="M405,305 L525,198 L650,192 L650,360 L405,388 Z"/>

  <!-- lower band -->
  <path class="lower-band" fill="var(--band)"
        d="M50,520 L1712,520 L1725,640 L1540,640 A130,130 0 0 0 1280,640 L460,640 A135,135 0 0 0 190,640 L50,640 Z"/>
  <rect class="web-strip" x="470" y="588" width="810" height="46" fill="var(--body)"/>

  <!-- lights -->
  <path class="headlight" fill="#d9dadc" stroke="#555" stroke-width="2" d="M92,435 L215,395 L200,470 L95,470 Z"/>
  <path class="indicator" fill="#e07a2e" d="M160,455 L190,420 L195,450 Z"/>
  <path class="taillight" fill="var(--tail)" d="M1672,330 L1705,325 L1708,505 L1674,505 Z"/>

  <!-- wheels -->
  <g class="wheel">
    <circle cx="325" cy="655" r="105" fill="var(--tyre)"/>
    <circle cx="325" cy="655" r="68" fill="var(--hub)"/>
    <circle cx="325" cy="655" r="14" fill="#8d9093"/>
  </g>
  <g class="wheel">
    <circle cx="1410" cy="655" r="105" fill="var(--tyre)"/>
    <circle cx="1410" cy="655" r="68" fill="var(--hub)"/>
    <circle cx="1410" cy="655" r="14" fill="#8d9093"/>
  </g>

  <!-- lettering -->
  <text class="headline" x="730" y="116">Wir sanieren Bäder.</text>

  <g class="brand">
    <rect x="790" y="200" width="44" height="44" fill="var(--stripe-dark)"/>
    <text class="brand-name" x="850" y="238">WENDELKAMP</text>
    <text class="brand-name" x="850" y="300" style="font-size:36px">Warendorf</text>
  </g>

  <g class="phone">
    <path fill="var(--ink)" d="M788,380 q6,-4 10,2 l6,10 q2,5 -3,8 l-4,3 q3,8 9,14 l3,-4 q4,-4 8,-1 l9,6 q5,4 1,10 l-4,5 q-6,5 -16,-2 q-14,-12 -22,-30 q-4,-13 3,-21 z"/>
    <text class="phone-number" x="822" y="400">015774620918</text>
  </g>

  <text class="address" x="432" y="415">Am Mühlenbach 7,</text>
  <text class="address" x="432" y="436">48231 Warendorf</text>

  <text class="website" x="975" y="621" text-anchor="middle">www.wendelkamp-badsanierungen.de</text>
</svg>
</body>
</html>
```